electrical automation company needs a letterhead design

we need a letter head designed for our new electrical automation company. Our company color are orange and blue as you'll see from our logo attached

Target Market(s)

Domestic, commercial and industrial electrical clients

Industry/Entity Type

Electrical

Contact Information for Business Card

I need to update my business card to make it more eye catching I have attached my old business card designs, logo and new trifold brochure to give you an idea

Font styles to use
Sans Serif

Colors
f37122
0393ce

Requirements
Must have
• larkfield electrical logo
my name
phone number
email
website
Nice to have
• QR code linked to my website
list of some services
- domestic
- commercial
- industrial

```html
<!DOCTYPE html>
<html lang="en">
<head>
<meta charset="utf-8">
<title>Larkfield Electrical – Letterhead</title>
<link rel="stylesheet" href="https://fonts.googleapis.com/css2?family=Open+Sans:wght@400;600;700&family=Arimo:wght@400;700&display=swap">
<style>
  :root {
    --brand-blue: #0474bc;
    --brand-orange: #f37122;
    --ink: #4a4a4a;
    --ink-dark: #333333;
    --paper: #ffffff;
  }
  * { margin: 0; padding: 0; box-sizing: border-box; }
  html, body { width: 1040px; height: 1200px; overflow: hidden; background: var(--paper); }
  .letterhead {
    position: relative;
    width: 1040px;
    height: 1200px;
    background: var(--paper);
    font-family: "Open Sans", sans-serif;
    color: var(--ink);
  }
  .brand {
    position: absolute;
    top: 74px;
    left: 0;
    width: 100%;
    display: flex;
    justify-content: center;
    align-items: center;
    gap: 14px;
  }
  .brand-dot {
    width: 34px;
    height: 34px;
    border-radius: 50%;
    background: var(--brand-orange);
  }
  .brand-name {
    font-weight: 700;
    font-size: 30px;
    letter-spacing: 0.5px;
    color: var(--brand-blue);
    text-transform: uppercase;
  }
  .letter {
    position: absolute;
    left: 97px;
    width: 841px;
    font-size: 15.5px;
    line-height: 18px;
  }
  .issue-date { top: 218px; }
  .recipient { top: 254px; font-style: normal; }
  .salutation { top: 358px; }
  .body-copy { top: 408px; }
  .body-copy p {
    line-height: 27px;
    text-align: justify;
    hyphens: auto;
    -webkit-hyphens: auto;
    margin-bottom: 27px;
  }
  .closing { top: 816px; }
  .signatory { top: 890px; }
  .signatory-name {
    font-size: 19px;
    font-weight: 600;
    color: var(--ink-dark);
    line-height: 26px;
  }
  .signatory-role { font-size: 15px; line-height: 22px; }
  .contact-band {
    position: absolute;
    top: 1122px;
    left: 0;
    width: 100%;
    height: 40px;
    background: var(--brand-blue);
    color: #ffffff;
    font-family: "Arimo", sans-serif;
    font-size: 18px;
    display: flex;
    justify-content: center;
    align-items: center;
    gap: 8px;
  }
  .contact-band b { font-weight: 700; }
  .services {
    position: absolute;
    top: 1166px;
    left: 0;
    width: 100%;
    height: 30px;
    display: flex;
    justify-content: center;
    align-items: center;
    gap: 8px;
    font-family: "Arimo", sans-serif;
    font-size: 18px;
    color: #222222;
  }
  .service-sep {
    width: 13px;
    height: 13px;
    border-radius: 50%;
    background: var(--brand-orange);
  }
</style>
</head>
<body>
  <main class="letterhead">
    <header class="brand">
      <span class="brand-dot"></span>
      <span class="brand-name">Larkfield Electrical</span>
    </header>

    <p class="letter issue-date">Issuing Date: May 5, 2018</p>

    <address class="letter recipient">
      Name Of Employee Mr. XYZABC<br>
      Address of Employee<br>
      Address Line 2 etc..
    </address>

    <p class="letter salutation">Dear Mr.XYZABC</p>

    <section class="letter body-copy" lang="en">
      <p>Lorem Ipsum has been the industry's standard dummy text ever since the 1500s, when an unknown printer took a galley of type and scrambled it to make a type specimen book. It has survived not only five centuries, but also the leap into electronic typesetting, remaining essentially unchanged. It was popularised in the 1960s with the release of Lettrex sheets containing Lorem Ipsum passages, and more recently with desktop publishing software like Quillset Pagecraft including versions of Lorem Ipsum.</p>
      <p>Lorem Ipsum is simply dummy text of the printing and typesetting industry. Lorem Ipsum has been the industry's standard dummy text ever since the 1500s, when an unknown printer took a galley of type and scrambled it to make a type specimen book.</p>
      <p>It has survived not only five centuries, but also the leap into electronic typesetting, remaining essentially unchanged. It was popularised in the 1960s with the release of Lettrex sheets containing Lorem IpsumIpsum passages.</p>
    </section>

    <p class="letter closing">Yours Sincerely</p>

    <div class="letter signatory">
      <p class="signatory-name">Daniel Harrow</p>
      <p class="signatory-role">Managing Director</p>
    </div>

    <footer>
      <div class="contact-band">
        <span><b>P:</b> 044-555 010 234</span>
        <span>|</span>
        <span><b>E:</b> info@larkfieldelec.com</span>
        <span>|</span>
        <span>www.larkfieldelec.com</span>
      </div>
      <div class="services">
        <span>DOMESTIC</span>
        <span class="service-sep"></span>
        <span>COMMERCIAL</span>
        <span class="service-sep"></span>
        <span>INDUSTRIAL</span>
      </div>
    </footer>
  </main>
</body>
</html>
```